Business Card Design Project

I need a business card designed from scratch. I have an existing logo that I can upload in Illustrator for modification or redesign.

The Company is called Ranking Oracles http://rankingoracles.com.au and we provide Search Engine Optimization services to Australian businesses. The current logo signifies an increase in visitors, profits etc...

There are no restrictions as to the redesign - colours, style etc are all open to change.

Cards will be full colour and one sided printed at http://www.cardmillo.com.au so check their requirements for file format and sizes etc.

I will expect all original files upon completion of project.

Target Market(s)

Any business with a web site looking to improve their search engine rankings

Industry/Entity Type

Business

Requirements
Must have
• I like modern, sleek designs. Clean, not fussy, uncluttered.

```html
<!DOCTYPE html>
<html lang="en">
<head>
<meta charset="utf-8">
<title>Ranking Oracles – Business Card</title>
<link href="https://fonts.googleapis.com/css2?family=Arimo:wght@400;700&display=swap" rel="stylesheet">
<style>
  :root {
    --page-bg: #ffffff;
    --card-white: #ffffff;
    --brand-blue: #1f78c1;
    --deep-blue: #0f3f74;
    --mid-blue: #1c6fb5;
    --accent-yellow: #f6c619;
    --name-blue: #2386cb;
    --title-grey: #555555;
    --contact-white: #ffffff;
  }
  html, body {
    margin: 0;
    padding: 0;
    width: 1200px;
    height: 901px;
    overflow: hidden;
    background: var(--page-bg);
    font-family: "Arimo", Arial, sans-serif;
  }
  .business-card {
    position: absolute;
    left: 112px;
    top: 166px;
    width: 978px;
    height: 551px;
    background: var(--card-white);
    box-shadow: 0 4px 10px rgba(0,0,0,0.35);
    overflow: hidden;
  }
  .card-artwork {
    position: absolute;
    inset: 0;
  }
  .brand-name {
    position: absolute;
    left: 60px;
    top: 112px;
    display: flex;
    align-items: center;
    gap: 16px;
    font-weight: 700;
    font-size: 50px;
    color: var(--brand-blue);
    letter-spacing: -0.5px;
  }
  .brand-dot {
    width: 34px;
    height: 34px;
    border-radius: 50%;
    background: var(--accent-yellow);
  }
  .person {
    position: absolute;
    left: 63px;
    top: 325px;
  }
  .person-name {
    margin: 0;
    font-size: 31px;
    font-weight: 700;
    color: var(--name-blue);
    line-height: 1.1;
  }
  .person-title {
    margin: 10px 0 0;
    font-size: 25px;
    color: var(--title-grey);
  }
  .contact-block {
    position: absolute;
    right: 45px;
    top: 256px;
    text-align: right;
    color: var(--contact-white);
    font-size: 25px;
    line-height: 36px;
  }
  .address { margin: 0 0 6px; }
  .contact-list {
    list-style: none;
    margin: 0;
    padding: 0;
  }
  .contact-item {
    display: flex;
    justify-content: flex-end;
    align-items: center;
    gap: 10px;
    height: 33px;
  }
  .contact-icon {
    width: 20px;
    height: 20px;
    flex: none;
  }
</style>
</head>
<body>
  <div class="business-card">
    <svg class="card-artwork" viewBox="0 0 978 551" width="978" height="551" aria-hidden="true">
      <defs>
        <linearGradient id="blueField" x1="0" y1="1" x2="1" y2="0">
          <stop offset="0" stop-color="#1f88d0"/>
          <stop offset="0.5" stop-color="var(--mid-blue)"/>
          <stop offset="1" stop-color="var(--deep-blue)"/>
        </linearGradient>
      </defs>
      <path class="accent-swoosh" fill="var(--accent-yellow)"
        d="M690,0 L770,0 C710,160 630,300 440,390 C310,450 160,470 0,470 L0,390
           C130,440 300,425 440,335 C575,250 650,120 690,0 Z"/>
      <path class="blue-field" fill="url(#blueField)"
        d="M752,0 L978,0 L978,551 L0,551 L0,445
           C160,470 340,455 470,380 C620,290 700,150 752,0 Z"/>
    </svg>

    <div class="brand-name"><span class="brand-dot"></span>Ranking Oracles</div>

    <div class="person">
      <p class="person-name">Daniel Whitford</p>
      <p class="person-title">Founder &amp; CEO</p>
    </div>

    <div class="contact-block">
      <p class="address">1187 Harbor Crest Way #204<br>Tampa, FL 33602</p>
      <ul class="contact-list">
        <li class="contact-item">1300 555 018
          <svg class="contact-icon" viewBox="0 0 20 20"><path fill="var(--accent-yellow)" d="M4 2l3 0 2 5-2 1.5c1 2 2.5 3.5 4.5 4.5L13 11l5 2v3c0 1-1 2-2 2C8 18 2 12 2 4c0-1 1-2 2-2z"/></svg>
        </li>
        <li class="contact-item">1300 555 018
          <svg class="contact-icon" viewBox="0 0 20 20"><rect x="5" y="1" width="10" height="18" rx="2" fill="var(--accent-yellow)"/><rect x="7" y="4" width="6" height="9" fill="var(--deep-blue)"/><circle cx="10" cy="16" r="1.2" fill="var(--deep-blue)"/></svg>
        </li>
        <li class="contact-item">1300 555 018
          <svg class="contact-icon" viewBox="0 0 20 20"><rect x="5" y="2" width="10" height="5" fill="var(--accent-yellow)"/><rect x="1" y="7" width="18" height="8" rx="1.5" fill="var(--accent-yellow)"/><rect x="5" y="12" width="10" height="6" fill="var(--accent-yellow)" stroke="var(--deep-blue)" stroke-width="1"/></svg>
        </li>
        <li class="contact-item">enquiry@rankingoracles.com.au
          <svg class="contact-icon" viewBox="0 0 20 20"><rect x="1" y="4" width="18" height="12" rx="1" fill="var(--accent-yellow)"/><path d="M1.5 4.5L10 11l8.5-6.5" fill="none" stroke="var(--deep-blue)" stroke-width="1.5"/></svg>
        </li>
        <li class="contact-item">www.rankingoracles.com.au
          <svg class="contact-icon" viewBox="0 0 20 20"><circle cx="10" cy="10" r="8.5" fill="var(--accent-yellow)"/><g fill="none" stroke="var(--deep-blue)" stroke-width="1.2"><ellipse cx="10" cy="10" rx="3.5" ry="8.5"/><path d="M1.5 10h17M3 5.5h14M3 14.5h14"/></g></svg>
        </li>
      </ul>
    </div>
  </div>
</body>
</html>
```